Web Design for an Online Dating Web Site

We need an uncoded web design for a new online dating web site called zMatchy.net. Simplicity and boldness are the key factors in the successful design.
Please look at the requirements document attached for details.
Updates
Dear all,
Please AVOID USING A PICTURE OF A HAPPY COUPLE ON THE HOME PAGE of the site. We highly want to move away from this space as it makes our web site just like another dating web site.
We like something simple with web 2.0 look and feel. The examples in the Requirements Document are exactly the design we are after.
Regards
Tarn
Industry/Entity Type
Dating
Look and feel
Each slider illustrates characteristics of the customer's brand and the style your logo design should communicate.

```html
<!DOCTYPE html>
<html lang="en">
<head>
<meta charset="utf-8">
<title>zMatchy.net – Member Home</title>
<link rel="stylesheet" href="https://fonts.googleapis.com/css2?family=Signika:wght@400;600;700&family=PT+Sans:wght@400;700&display=swap">
<style>
:root{
  --lime:#a6e84a;
  --lime-dark:#8fd234;
  --pink:#e8177f;
  --pink-soft:#f26aa8;
  --sky-top:#c9ecfb;
  --sky-bottom:#4ccaf0;
  --ink:#3f3f3f;
  --ink-soft:#555;
  --white:#ffffff;
  --date-blue:#2fa8cf;
  --menu-top:#f2f2f2;
  --menu-bottom:#b9b9b9;
  --footer-top:#9d9d9f;
  --footer-bottom:#6e6e70;
  --field:#5f5f61;
  --field-text:#e9e9e9;
}
*{margin:0;padding:0;box-sizing:border-box}
html,body{width:800px;height:1200px;overflow:hidden}
body{position:relative;background:var(--white);font-family:"PT Sans",sans-serif;color:var(--ink)}
.abs{position:absolute}

.top-bar{left:0;top:0;width:800px;height:105px;background:linear-gradient(#b3ee5a,var(--lime))}
.top-nav{right:35px;top:18px;display:flex;gap:26px;font-family:"Signika",sans-serif;font-weight:600;font-size:23px;letter-spacing:1.5px}
.top-nav .welcome{color:var(--white)}
.top-nav a{color:var(--ink);text-decoration:none}
.sign-out{left:693px;top:61px;width:80px;height:22px;border-radius:4px;background:linear-gradient(#8fdcf8,#35b7e6);color:var(--white);font-family:"Signika",sans-serif;font-size:12px;font-weight:600;text-align:center;line-height:22px;letter-spacing:.5px}

.brand-band{left:0;top:105px;width:800px;height:150px;background:linear-gradient(#fff 70%,#e9f6fd)}
.brand{left:50px;top:138px;display:flex;align-items:center;gap:14px}
.brand-dot{width:26px;height:26px;border-radius:50%;background:var(--pink)}
.brand-name{font-family:"Signika",sans-serif;font-weight:600;font-size:66px;color:var(--pink);line-height:1}
.stuff-tab{left:507px;top:206px;width:266px;height:46px;border-radius:10px 10px 0 0;background:linear-gradient(#b6ef63,var(--lime-dark));font-family:"Signika",sans-serif;font-size:28px;color:var(--ink);text-align:center;line-height:50px}
.divider{left:0;top:254px;width:800px;height:4px;background:#8c9aa2}

.stage{left:0;top:258px;width:800px;height:620px;background:linear-gradient(var(--sky-top),#86d9f6 60%,var(--sky-bottom))}
.stuff-menu{left:543px;top:258px;width:205px;height:207px;background:linear-gradient(var(--menu-top),var(--menu-bottom));box-shadow:0 2px 4px rgba(0,0,0,.3);list-style:none;padding:16px 0 0 27px}
.stuff-menu li{font-size:18px;color:var(--ink-soft);height:36px;line-height:22px}

.messages-tab{left:40px;top:487px;width:412px;height:56px;border-radius:12px 12px 0 0;background:linear-gradient(#f03a94,var(--pink))}
.messages-title{left:144px;top:497px;font-family:"Signika",sans-serif;font-weight:700;font-size:30px;color:var(--white);letter-spacing:1.5px}
.badge{left:373px;top:504px;width:28px;height:28px;border-radius:50%;background:var(--lime);font-family:"Signika",sans-serif;font-weight:700;font-size:18px;color:var(--ink);text-align:center;line-height:28px}
.badge-label{left:405px;top:508px;font-size:14px;color:var(--ink)}

.messages-card{left:22px;top:540px;width:448px;height:311px;border-radius:14px;background:linear-gradient(#fff 75%,#e4f4fc);border:3px solid var(--white);box-shadow:0 0 0 1px #bfe6f6}
.message{position:absolute;left:12px;width:420px;height:92px}
.message.unread{background:#ededed;border-radius:10px}
.avatar{position:absolute;left:8px;top:8px;width:82px;height:75px;border-radius:10px;border:3px solid #b9b9b9}
.avatar.blue{background:linear-gradient(#bfe8fb,#48c0ec)}
.avatar.pink{background:linear-gradient(#fbd4e6,#ee5fa3)}
.message time{position:absolute;right:18px;top:19px;font-size:14.5px;color:var(--date-blue);letter-spacing:.3px}
.message p{position:absolute;left:118px;top:43px;font-size:15px;color:#444}
.message.read p.faded{color:#7a7a7a}

.stage-rule{left:509px;top:573px;width:3px;height:208px;background:linear-gradient(#e9f8ff,#b8ecfd)}
.mascots{left:522px;top:585px;width:258px;height:190px;border-radius:40px;background:radial-gradient(circle at 30% 35%,#aee4f8 0 25%,transparent 26%),radial-gradient(circle at 78% 55%,#f064a6 0 20%,transparent 21%),linear-gradient(transparent 80%,#8fdcf6)}
.cta{left:549px;top:790px;width:224px;height:52px;border-radius:10px;background:linear-gradient(#bdf06c,var(--lime-dark));box-shadow:0 1px 3px rgba(0,0,0,.25);font-family:"Signika",sans-serif;font-weight:600;font-size:24px;letter-spacing:1.5px;color:var(--ink);text-align:center;line-height:54px}

.footer{left:0;top:878px;width:800px;height:322px;background:linear-gradient(var(--footer-top),var(--footer-bottom));border-top:3px solid #6a6a6a}
.footer-heading{font-family:"Signika",sans-serif;font-weight:600;font-size:28px;color:#2d2d2d;letter-spacing:1.5px}
.read-more{left:76px;top:916px}
.read-rule{left:45px;top:955px;width:216px;height:1px;background:#5a5a5a}
.links{left:89px;top:962px;list-style:none}
.links li{font-family:"Signika",sans-serif;font-size:17px;letter-spacing:1.5px;color:#ececec;height:28px;line-height:26px}
.lets-talk{left:343px;top:918px}
.field{background:var(--field);color:var(--field-text);font-size:20px;padding:6px 9px}
.f-name{left:338px;top:965px;width:206px;height:35px}
.f-email{left:338px;top:1011px;width:206px;height:35px}
.f-message{left:338px;top:1059px;width:208px;height:113px}
.foot-brand{left:600px;top:1128px;display:flex;align-items:center;gap:7px}
.foot-brand .brand-dot{width:12px;height:12px}
.foot-brand .brand-name{font-size:34px}
</style>
</head>
<body>
  <header class="top-bar abs"></header>
  <nav class="top-nav abs">
    <span class="welcome">Welcome, Rowan77</span>
    <a href="#">Start Dating!</a>
    <a href="#">Help</a>
  </nav>
  <div class="sign-out abs">Sign Out</div>

  <div class="brand-band abs"></div>
  <div class="brand abs"><span class="brand-name">zMatchy</span><span class="brand-dot"></span></div>
  <div class="stuff-tab abs">My Stuff</div>
  <div class="divider abs"></div>

  <main class="stage abs"></main>
  <ul class="stuff-menu abs">
    <li>My Details</li>
    <li>My Seeking Criteria</li>
    <li>My Avatar</li>
    <li>My Video</li>
    <li>My Friends</li>
  </ul>

  <div class="messages-tab abs"></div>
  <h2 class="messages-title abs">My Messages</h2>
  <span class="badge abs">2</span>
  <span class="badge-label abs">new!</span>

  <section class="messages-card abs">
    <article class="message unread" style="top:6px">
      <div class="avatar blue" role="img" aria-label="Member avatar placeholder"></div>
      <time>Wednesday&nbsp; Oct. 5, 2011</time>
      <p>“Hi, I saw your profile picture and I was...”</p>
    </article>
    <article class="message read" style="top:102px">
      <div class="avatar pink" role="img" aria-label="Member avatar placeholder"></div>
      <time>Saturday&nbsp; Oct. 1, 2011</time>
      <p>“LOL, that’s fantastic!”</p>
    </article>
    <article class="message read" style="top:196px">
      <div class="avatar pink" role="img" aria-label="Member avatar placeholder"></div>
      <time>Monday&nbsp; Sep. 12, 2011</time>
      <p class="faded">“Hey, I just got your message, very nice...”</p>
    </article>
  </section>

  <div class="stage-rule abs"></div>
  <div class="mascots abs" role="img" aria-label="Illustration of two speech-bubble mascots, one blue and one pink"></div>
  <div class="cta abs">Start Dating!</div>

  <footer class="footer abs"></footer>
  <h3 class="footer-heading read-more abs">Read More</h3>
  <div class="read-rule abs"></div>
  <ul class="links abs">
    <li>Why zMatchy,</li>
    <li>How it works,</li>
    <li>Sign Up,</li>
    <li>Login,</li>
    <li>About Us</li>
  </ul>
  <h3 class="footer-heading lets-talk abs">Let’s Talk</h3>
  <div class="field f-name abs">Name</div>
  <div class="field f-email abs">Email</div>
  <div class="field f-message abs">Message</div>
  <div class="foot-brand abs"><span class="brand-name">zMatchy</span><span class="brand-dot"></span></div>
</body>
</html>
```